Australian Consulting Business Specialising in People and Process Consulting with Bluechip clients n

We are looking for designs using the logo as attached for letterhead and business cards that can be carried through to website in order to achieve consistency of style and hence recognition. It does not have to be overly suggestive but rather clean, crisp and professional.

The details are as follows:
Business Cards

Front Side
Brett Halloran
Director
M. 0427 305 612
E. brett@pinnockhallorran.com.au
W. www.pinnockhalloran.com.au

Warren pinnock
Director
M. 0433 571 920
E. warren@pinnockhallorran.com.au

Business Cards
Flip Side
Key Offerings

People Culture Process Growth
Development Analytics Improvement Strategies

Letter Head Details
Logo
Corporate Details
Pinnock Halloran Pty Ltd
PO Box 83
Kelvindale VIC 3287
Tel 61 3 9274 5808
info@pinnockhalloran.com.au
ACN 253917604
ABN 72016458391

```html
<!DOCTYPE html>
<html lang="en">
<head>
<meta charset="utf-8">
<title>Pinnock Halloran – Business Card</title>
<link href="https://fonts.googleapis.com/css2?family=Montserrat:wght@600;700&family=Open+Sans:wght@400;600&display=swap" rel="stylesheet">
<style>
  :root{
    --bg:#e9e7e3;
    --card:#ffffff;
    --blue:#1273bd;
    --orange:#f7931e;
    --grey:#555a60;
    --red:#c8102e;
    --icon:#6b6e72;
    --faint-grey:#dcdcdf;
    --faint-blue:#c4dcef;
    --faint-orange:#fde3c6;
  }
  *{box-sizing:border-box;margin:0;padding:0}
  html,body{width:1200px;height:1000px;overflow:hidden;background:var(--bg)}
  .canvas{position:relative;width:1200px;height:1000px}

  .card{position:absolute;left:210px;width:780px;height:430px;background:var(--card);
        box-shadow:0 6px 18px rgba(0,0,0,.18);overflow:hidden}

  /* front */
  .card-front{top:40px;border-radius:70px 0 70px 0}
  .front-top-band{position:absolute;top:0;right:0;width:58%;height:12px;
        background:linear-gradient(to left,var(--orange),rgba(247,147,30,0))}
  .front-bottom-band{position:absolute;bottom:0;left:0;width:58%;height:12px;
        background:linear-gradient(to right,var(--blue),rgba(18,115,189,0))}
  .holder{position:absolute;top:44px;right:30px;text-align:right}
  .holder-role{font:400 16px "Open Sans",Arial,sans-serif;color:#222;margin-bottom:6px;margin-right:6px}
  .holder-name{display:inline-block;background:var(--blue);color:#fff;
        font:400 23px "Open Sans",Arial,sans-serif;padding:6px 18px 6px 30px}
  .brand{position:absolute;left:200px;top:180px;display:flex;align-items:center;gap:14px}
  .brand-dot{width:56px;height:56px;border-radius:50%;background:var(--blue)}
  .brand-name{font:700 36px "Montserrat",Arial,sans-serif;color:var(--blue);letter-spacing:.5px;line-height:1}
  .brand-tagline{font:600 11.5px "Montserrat",Arial,sans-serif;color:var(--grey);letter-spacing:4.2px;margin-top:6px}
  .contacts{position:absolute;left:26px;bottom:30px;list-style:none}
  .contacts li{display:flex;align-items:center;gap:8px;font:400 14px "Open Sans",Arial,sans-serif;
        color:var(--red);letter-spacing:1.5px;line-height:21px}
  .contacts svg{width:13px;height:13px;flex:none}

  /* back */
  .card-back{top:510px;border-radius:0 0 60px 0}
  .back-circle{position:absolute;left:50%;top:50%;width:300px;height:300px;margin:-150px 0 0 -150px;
        border-radius:50%;background:var(--faint-grey)}
  .offerings{position:absolute;left:0;right:0;top:168px;text-align:center;font-family:"Open Sans",Arial,sans-serif}
  .offerings-title{font-weight:600;font-size:24px;color:#1d5fae;letter-spacing:2.5px;margin-bottom:10px}
  .offerings-list{font-size:18px;color:#333;line-height:26px}
</style>
</head>
<body>
<div class="canvas">

  <section class="card card-front" aria-label="Business card front">
    <div class="front-top-band"></div>
    <div class="holder">
      <p class="holder-role">Director</p>
      <p class="holder-name">Warren pinnock</p>
    </div>
    <div class="brand">
      <span class="brand-dot"></span>
      <div>
        <p class="brand-name">PINNOCK HALLORAN</p>
        <p class="brand-tagline">PEOPLE AND PROCESS CONSULTANTS</p>
      </div>
    </div>
    <ul class="contacts">
      <li><svg viewBox="0 0 14 14"><circle cx="7" cy="7" r="7" fill="var(--icon)"/><path d="M4.5 3.5l1.5 1.8-.8 1c.5 1 1.3 1.8 2.3 2.3l1-.8 1.8 1.5-.9 1.2C6.5 10.3 3.7 7.5 3.4 4.4z" fill="#fff"/></svg>0433 571 920</li>
      <li><svg viewBox="0 0 14 14"><circle cx="7" cy="7" r="7" fill="var(--icon)"/><circle cx="7" cy="7" r="2.8" fill="none" stroke="#fff" stroke-width="1.3"/></svg>warren@pinnockhallorran.com.au</li>
      <li><svg viewBox="0 0 14 14"><circle cx="7" cy="7" r="7" fill="var(--icon)"/><rect x="3.5" y="4" width="7" height="6" rx="1" fill="none" stroke="#fff" stroke-width="1.2"/></svg>www.pinnockhalloran.com.au</li>
    </ul>
    <div class="front-bottom-band"></div>
  </section>

  <section class="card card-back" aria-label="Business card back">
    <div class="back-circle"></div>
    <div class="offerings">
      <h2 class="offerings-title">KEY OFFERINGS</h2>
      <p class="offerings-list">People Culture Process Growth<br>Development Analytics Improvement Strategies</p>
    </div>
  </section>

</div>
</body>
</html>
```